Company Business Card Design Project - Revamp the image of an old construction company.

We need a business card designed for a new company in Australia.

Type of business is Commercial Roofing & Painting.

Medium will be brushed black metal card that can/will be acid etched to a brushed steel silver, acid die cut and two printed colours of our choice which will be white and pantone orange.

We have hopes that the design will be simple, modern and represent with a quick glance what our company does.

Please read instructions carefully in must have box any questions please ask.

If you are interested in this job please look at other job that we have which is very similar with logo and design

Please have a look at the things that can be done with metals cards on yondle images for inspiration.

Target Market(s)

Business owners, commercial property development Men from 25-70 years of age.

Industry/Entity Type

Construction

Requirements
Must have
• Front of card:

Must use the company logo and name provided as attachment (see below kestrel mark construction_black_background).

the words -Commercial Painting and Roofing- must be on front of card

details needed on front or back depending on your design

Name
position
email
mobile

all details can be on front with a cool design to be etched on the back of card or to keep front simple you can put all detail on back of card, I will leave the lay out to you.

Colours in logo are

Pantone 144 C Orange
Pantone 11-0601 White
Pantone 7539 C Gray
Pantone 426 C Black

However black will be the base of black metal card. Gray will be replaced with the etching in card revealing the silver. Orange and white will be printed on card.

Please have fun!!
Should not have
• Please don't clutter the card
No fonts smaller then 7 points

```html
<!DOCTYPE html>
<html lang="en">
<head>
<meta charset="utf-8">
<title>Kestrel Mark Industries – Business Card</title>
<link href="https://fonts.googleapis.com/css2?family=Arimo:wght@400;700&display=swap" rel="stylesheet">
<style>
  :root {
    --page: #ffffff;
    --card: #231f20;
    --orange: #f7941d;
    --tag-orange: #f39a3b;
    --white: #ffffff;
    --steel: #a7a9ac;
    --note: #222222;
  }
  html, body {
    margin: 0;
    padding: 0;
    width: 1200px;
    height: 1000px;
    overflow: hidden;
    background: var(--page);
    font-family: "Arimo", Arial, sans-serif;
  }
  .sheet {
    position: relative;
    width: 1200px;
    height: 1000px;
  }
  .card {
    position: absolute;
    top: 360px;
    width: 385px;
    height: 199px;
    background: var(--card);
  }
  .card--front { left: 207px; }
  .card--back { left: 642px; }

  .brand {
    position: absolute;
    left: 24px;
    top: 50px;
    display: flex;
    align-items: center;
    gap: 16px;
  }
  .brand__mark {
    width: 72px;
    height: 72px;
    background: var(--steel);
  }
  .brand__name {
    font-weight: 700;
    font-size: 21px;
    line-height: 1.1;
    color: var(--orange);
    letter-spacing: 0.5px;
  }

  .contact {
    position: absolute;
    left: 53px;
    top: 38px;
    font-size: 14px;
    line-height: 16.3px;
    color: var(--white);
  }
  .contact p { margin: 0; white-space: nowrap; }
  .tagline {
    position: absolute;
    left: 53px;
    top: 143px;
    margin: 0;
    font-size: 13.6px;
    white-space: nowrap;
    color: var(--tag-orange);
  }
  .back-mark {
    position: absolute;
    left: 285px;
    top: 50px;
    width: 74px;
    height: 72px;
    background: var(--steel);
  }

  .spec {
    position: absolute;
    left: 0;
    width: 1234px;
    margin: 0;
    text-align: center;
    font-size: 13.6px;
    color: var(--note);
  }
  .spec--size { top: 577px; }
  .spec--cut { top: 609px; }
</style>
</head>
<body>
<main class="sheet">
  <section class="card card--front" aria-label="Card front">
    <div class="brand">
      <div class="brand__mark"></div>
      <div class="brand__name">KESTREL MARK<br>INDUSTRIES Pty Ltd</div>
    </div>
  </section>

  <section class="card card--back" aria-label="Card back">
    <div class="contact">
      <p>Liam Carver</p>
      <p>Managing Director</p>
      <p>email@kestrelmark.com</p>
      <p>02 555 018 274</p>
    </div>
    <p class="tagline">Commercial Roofing &amp; Painting</p>
    <div class="back-mark"></div>
  </section>

  <p class="spec spec--size">Height : 90mm * Width : 62mm</p>
  <p class="spec spec--cut">Recommended die cut on the black portion of logo icon.</p>
</main>
</body>
</html>
```